Become a real French Pastry chef with an easy 3 step pastry kit box.

The company is specialized in French pastries and the boxes will be sold online, and retail stores. The goal is for anyone who likes to be creative and crafty to create and bake their own traditional french pastry in 3 easy steps right at home. French pastries can be known to take hours to bake. These boxes allow you to make them very quickly, no hassle and they results taste amazing. All the ingredients are from FRANCE. Everything you need is in the box, All you need is water! The box design desired is elegant, simple, glamorous but yet eye catchy for retail distribution. This is a kit box with pre scaled ingredients to make your own eclairs. Box dimensions are 8x6x2.
Updates

Target Market(s)

Middle Aged, middle to upper class housewives who enjoy cooking and baking

Industry/Entity Type

Bakery

Font styles to use
Decorative
Script

Colors

Designer to choose colors to be used in the design.

Requirements
Must have
• This box will be called "The eclair kit by {logo}, or {logo} presents the Eclair kit.
• Has to have the instructions (attached document)
• "This box contains: 4 éclair shells, powder pouch, icing bag, pipping bag and pipping tip"
• Net weight 245g
• Nutrition label (attached)
Nice to have
• An eclair on it.

```html
<!DOCTYPE html>
<html lang="en">
<head>
<meta charset="utf-8">
<title>The Eclair Kit – Belcourt Bakery</title>
<link rel="stylesheet" href="https://fonts.googleapis.com/css2?family=Parisienne&family=Comfortaa:wght@400&family=Roboto+Condensed:wght@300&family=Courier+Prime:wght@400;700&family=Playfair+Display:ital,wght@1,700&display=swap">
<style>
  :root {
    --backdrop: #eeeeea;
    --panel: #ffffff;
    --frame: #d9d1d1;
    --ink: #1c1c1c;
    --soft-ink: #444444;
    --brand-blue: #3a6fb5;
    --flag-blue: #1f3f8f;
    --flag-red: #e0303a;
    --badge-green: #4f8a2a;
    --lilac: rgba(190, 165, 222, .75);
    --blush: rgba(246, 190, 206, .75);
    --butter: rgba(248, 216, 130, .7);
    --photo-warm: #c89766;
    --photo-light: #ead8c2;
  }
  * { box-sizing: border-box; margin: 0; padding: 0; }
  html, body { width: 1200px; height: 927px; overflow: hidden; background: var(--backdrop); }

  .box-lid {
    position: absolute; left: 110px; top: 105px; width: 980px; height: 717px;
    background: var(--panel); box-shadow: 0 18px 40px rgba(0,0,0,.12);
  }
  .frame { position: absolute; inset: 34px; border: 2px solid var(--frame); }
  .frame::after { content: ""; position: absolute; inset: 6px; border: 1px solid var(--frame); }

  .wash { position: absolute; inset: 0; pointer-events: none; }
  .wash-blob { position: absolute; border-radius: 50%; }
  .wash-blob--lilac-right { left: 520px; top: 115px; width: 240px; height: 170px;
    background: radial-gradient(closest-side, var(--lilac), transparent); }
  .wash-blob--lilac-left { left: 310px; top: 200px; width: 230px; height: 150px;
    background: radial-gradient(closest-side, var(--lilac), transparent); }
  .wash-blob--blush { left: 330px; top: 190px; width: 440px; height: 230px;
    background: radial-gradient(closest-side, var(--blush), transparent); }
  .wash-blob--butter { left: 400px; top: 330px; width: 170px; height: 90px;
    background: radial-gradient(closest-side, var(--butter), transparent); }

  .brand {
    position: absolute; left: 0; right: 0; top: 70px; text-align: center;
    font-family: "Parisienne", cursive; font-size: 38px; color: var(--brand-blue);
  }
  .brand-dot {
    display: inline-block; width: 10px; height: 10px; border-radius: 50%;
    background: var(--flag-red); vertical-align: middle; margin-right: 8px;
  }
  .presents {
    position: absolute; left: 0; right: 0; top: 140px; text-align: center;
    font-family: "Parisienne", cursive; font-size: 28px; color: var(--ink);
  }
  .kit-title {
    position: absolute; left: 0; right: 0; top: 172px; text-align: center;
    font-family: "Parisienne", cursive; font-weight: 400; font-size: 56px; color: var(--ink);
  }
  .tagline {
    position: absolute; left: 0; right: 0; top: 262px; text-align: center;
    font-family: "Comfortaa", sans-serif; font-size: 28px; color: var(--ink);
  }
  .eclair-photo {
    position: absolute; left: 360px; top: 330px; width: 310px; height: 130px; border-radius: 8px;
    background: radial-gradient(ellipse at 50% 50%, var(--photo-warm) 0%, var(--photo-light) 70%, var(--panel) 100%);
  }
  .net-weight {
    position: absolute; left: 0; right: 0; top: 490px; text-align: center;
    font-family: "Playfair Display", serif; font-style: italic; font-weight: 700;
    font-size: 19px; color: var(--ink);
  }

  .origin { position: absolute; left: 100px; top: 160px; width: 160px; text-align: center; }
  .origin svg { display: block; margin: 0 auto 10px; }
  .origin p {
    font-family: "Roboto Condensed", sans-serif; font-weight: 300; font-size: 17px;
    line-height: 1.15; color: var(--soft-ink);
  }
  .contents {
    position: absolute; left: 95px; top: 455px; padding: 7px 9px;
    border: 1px solid #8a8a8a;
    font-family: "Courier Prime", monospace; font-size: 13px; line-height: 1.25; color: var(--soft-ink);
    white-space: nowrap;
  }
  .contents strong { font-weight: 700; }
  .natural-seal { position: absolute; right: 100px; top: 330px; }
</style>
</head>
<body>
  <main class="box-lid">
    <div class="frame"></div>
    <div class="wash" role="img" aria-label="Soft watercolour wash in lilac, blush pink and butter yellow">
      <div class="wash-blob wash-blob--blush"></div>
      <div class="wash-blob wash-blob--lilac-right"></div>
      <div class="wash-blob wash-blob--lilac-left"></div>
      <div class="wash-blob wash-blob--butter"></div>
    </div>
    <div class="brand"><span class="brand-dot"></span>Belcourt Bakery</div>
    <p class="presents">presents</p>
    <h1 class="kit-title">the Eclair kit</h1>
    <p class="tagline">Create your own traditional french Eclair</p>
    <div class="eclair-photo" role="img" aria-label="Photo of two chocolate-glazed eclairs, one cut open to show cream filling"></div>
    <p class="net-weight">n/w 245g</p>

    <div class="origin">
      <svg width="54" height="40" viewBox="0 0 54 40" aria-hidden="true">
        <clipPath id="flag-shape"><ellipse cx="27" cy="20" rx="26" ry="19"/></clipPath>
        <g clip-path="url(#flag-shape)">
          <rect x="0" y="0" width="18" height="40" fill="var(--flag-blue)"/>
          <rect x="18" y="0" width="18" height="40" fill="#ffffff"/>
          <rect x="36" y="0" width="18" height="40" fill="var(--flag-red)"/>
        </g>
      </svg>
      <p>All the ingredients<br>are from FRANCE</p>
    </div>

    <div class="contents">
      <strong>contains</strong>: 4 éclair shells-<br>powder pouch-icing bag-<br>piping bag &amp; piping tip.
    </div>

    <svg class="natural-seal" width="100" height="100" viewBox="0 0 100 100" aria-hidden="true">
      <circle cx="50" cy="50" r="45" fill="none" stroke="var(--badge-green)" stroke-width="3"/>
      <circle cx="50" cy="50" r="36" fill="none" stroke="var(--badge-green)" stroke-width="1.5"/>
    </svg>
  </main>
</body>
</html>
```